COMPETITION TITLE:
Premium Skincare Packaging Design for Modern Hydration Beauty Brand
ABOUT THE PROJECT
We are developing a new skincare brand called VELORIQUE.
We are looking for a sophisticated and commercially strong packaging design direction for our initial skincare soft launch.
The brand positioning is:
* modern premium skincare
* hydration-focused
* wellness-oriented
* calming and elegant
* emotionally reassuring
* modern feminine skincare
* premium online beauty brand
The products are designed around hydration, skin comfort and modern skincare rituals.
The brand is inspired by modern hydration and skin wellness for people adapting between warmer and colder climates. The visual direction should therefore feel emotionally warm, comforting and restorative while remaining modern, refined and internationally premium rather than overtly cultural or decorative.
WHAT WE NEED
We are primarily seeking the VISUAL DIRECTION and PACKAGING IDENTITY for one hero product:
LIGHT MOISTURISING DAY CREAM
The winning visual direction will later be adapted across additional products within the range, including:
* Brightening Eye Cream
* Hydrating Mist / Toner
Therefore we are looking for a cohesive skincare brand identity system rather than unrelated individual designs.
IMPORTANT PACKAGING INFORMATION
The product packaging is:
* white plastic pump dispenser bottle
* transparent clear plastic lid
* outer cardboard carton/box
Bottle dimensions:
* diameter: 30mm
* total height including lid: 147mm
* bottle body height: approx. 120mm
* transparent lid height: approx. 27mm
Outer carton dimensions:
* height: 150mm
* width: 40mm x 35mm
IMPORTANT:
The packaging itself is minimalist and lightweight, therefore the LABEL DESIGN and OVERALL BRAND DIRECTION should visually elevate the product and make it feel:
* premium
* substantial
* calming
* elegant
* modern
* trustworthy
* emotionally warm
* intentional
The design should help the packaging feel significantly more premium than standard mass-market skincare.
FILES PROVIDED
We are providing:
* bottle label template
* outer box template
* logo/icon
* packaging dimensions
The supplied logo/icon should be retained conceptually, however designers may professionally refine and recreate/vectorise the artwork where required for packaging consistency and premium presentation.
At this stage we are NOT looking for final technical production artwork.
We are primarily looking for:
* visual direction
* typography
* colour palette
* premium skincare aesthetic
* realistic product mockups
IMPORTANT WEBSITE NOTE
A current website link may be provided for background information only.
Please DO NOT take heavy visual inspiration from the existing website design, as the website itself is expected to evolve in the future alongside the packaging direction.
The packaging design should therefore LEAD the future visual identity of the brand rather than follow the current website styling.
DESIGN STYLE
We are looking for:
* modern premium wellness skincare
* understated luxury
* elegant typography
* emotionally warm but clean branding
* hydration-focused beauty aesthetic
* premium online skincare look
The product should feel:
* calming when held
* emotionally reassuring rather than clinical
* modern wellness rather than minimalist pharmacy
* elegant but human rather than cold luxury
* comforting and restorative rather than cosmetic-only
Subtle texture, tonal layering and sophisticated visual depth are encouraged where appropriate.
Designers are encouraged to create a recognisable and distinctive visual identity rather than generic minimalist skincare packaging.
PLEASE AVOID
* gold luxury clichés
* ornate decorative themes
* floral overload
* influencer-style beauty branding
* overly clinical pharmacy aesthetics
* generic Plindo-style layouts
* packaging that feels cold or sterile
STYLE REFERENCES
Please take inspiration from brands such as:
* Mirova
* Bright Petal
* Coravel
* Grace of Kellmar
We particularly like:
* elegant spacing
* clean premium typography
* calm colour palettes
* subtle luxury
* modern hydration skincare aesthetics
COLOUR DIRECTION
Preferred tones include:
* warm ivory
* soft cream
* muted blush
* sand
* charcoal typography
* subtle deep plum accents
* restrained muted rose-gold accents
Please avoid:
* neon colours
* excessive metallic effects
* harsh black-and-white pharmacy styling
* very dark packaging
IMPORTANT DESIGN NOTE
The slim vertical packaging should feel intentionally elegant and premium rather than small or sample-sized.
The label design should visually elongate and elevate the packaging.
LOGO
An existing logo/icon is provided and should be retained and integrated into the design direction rather than completely redesigned.
DELIVERABLES
We are looking for:
* one fully developed hero product design
* realistic bottle + outer box mockups
* coordinated visual direction suitable for future product extensions
* typography and colour direction
* editable source files
The final approved visual system will later be adapted across additional products within the range.
BRAND NAME
VELORIQUE
OPTIONAL TAGLINE DIRECTION
Climate Adapt Hydration
Updates
Thank you everyone for the submissions so far — there are some very strong directions emerging.
A few important thoughts as the project develops:
We are looking not only for attractive skincare labels, but for a distinctive and recognisable BRAND IDENTITY that could grow with the business over time across future packaging formats including larger cartons, jars and premium skincare packaging.
One area we would particularly encourage designers to explore further is refinement/elevation of the existing logo/icon. We would like to retain the core rose/circle concept, however subtle refinement, balance, geometry, typography pairing and premium presentation are encouraged where appropriate.
The strongest directions for us so far are those that feel:
* emotionally warm rather than clinical
* modern premium wellness rather than generic minimal skincare
* calming and reassuring when viewed or held
* elegant and distinctive rather than trend-driven
* premium without relying on gold luxury clichés
We are especially interested in designs that create a memorable visual identity system rather than simply placing text onto a white skincare bottle.
Subtle tonal layering, refined typography, understated sophistication and intelligent visual restraint are all encouraged.
Many thanks again and we are very excited to see the next round of directions develop.

```html
<!DOCTYPE html>
<html lang="en">
<head>
<meta charset="utf-8">
<title>VELORIQUE – Light Moisturising Day Cream Packaging</title>
<link rel="stylesheet" href="https://fonts.googleapis.com/css2?family=Cormorant+SC:wght@500&family=Jost:wght@300;400&display=swap">
<style>
  :root {
    --bg: #efe6dc;
    --ivory: #f8f4ee;
    --carton: #f3eee7;
    --side: #ece5dc;
    --charcoal: #3a302c;
    --plum: #8e5e66;
    --blush: #d9b3b3;
    --line: #b38d78;
  }
  * { margin: 0; padding: 0; box-sizing: border-box; }
  html, body { width: 1200px; height: 1200px; overflow: hidden; }
  body {
    background: var(--bg);
    font-family: "Jost", sans-serif;
    color: var(--charcoal);
    position: relative;
  }
  .panel { position: absolute; overflow: hidden; text-align: center; }
  .bottle-label { left: 120px; top: 190px; width: 300px; height: 860px; background: var(--ivory); border-radius: 4px; }
  .carton-front { left: 480px; top: 80px; width: 440px; height: 1040px; background: var(--carton); }
  .carton-side { left: 920px; top: 80px; width: 150px; height: 1040px; background: var(--side); }

  .at { position: absolute; left: 0; right: 0; display: flex; flex-direction: column; align-items: center; z-index: 1; }

  .brand-mark { border-radius: 50%; background: var(--blush); border: 3px solid #5a4a3e; }
  .bottle-label .brand-mark { width: 76px; height: 76px; }
  .carton-front .brand-mark { width: 92px; height: 92px; }
  .brand-name { font-family: "Cormorant SC", serif; font-weight: 500; color: var(--charcoal); letter-spacing: 2px; line-height: 1; }
  .bottle-label .brand-name { font-size: 36px; }
  .carton-front .brand-name { font-size: 52px; }
  .brand-line { font-size: 8px; letter-spacing: 1.6px; text-transform: uppercase; }
  .carton-front .brand-line { font-size: 11px; letter-spacing: 2.2px; }
  .divider { width: 1px; background: var(--line); }
  .product-name { font-weight: 400; text-transform: uppercase; letter-spacing: 3px; line-height: 1.45; }
  .bottle-label .product-name { font-size: 17px; }
  .carton-front .product-name { font-size: 19px; }
  .tagline { color: var(--plum); text-transform: uppercase; letter-spacing: 2.4px; line-height: 1.6; }
  .bottle-label .tagline { font-size: 12px; }
  .carton-front .tagline { font-size: 13px; }
  .skin-types { font-weight: 300; line-height: 1.7; }
  .bottle-label .skin-types { font-size: 11px; }
  .carton-front .skin-types { font-size: 13px; }
  .motif { border-radius: 50%; background: radial-gradient(circle, #ead3cc, #d8b3ad); }
  .volume { font-weight: 300; }
  .bottle-label .volume { font-size: 13px; }
  .carton-front .volume { font-size: 15px; }

  .landscape { position: absolute; left: 0; right: 0; bottom: 0; z-index: 0;
    background: linear-gradient(180deg, rgba(241,223,219,0) 0%, #f0dcd8 18%, #dcb9b9 55%, #c4959c 100%); }
  .bottle-label .landscape { height: 260px; }
  .carton-front .landscape, .carton-side .landscape { height: 250px; }

  .benefit { position: absolute; left: 0; right: 0; display: flex; flex-direction: column; align-items: center; z-index: 1; }
  .benefit svg { width: 26px; height: 30px; fill: none; stroke: var(--charcoal); stroke-width: 1.2; }
  .benefit p { font-size: 10px; letter-spacing: 1px; text-transform: uppercase; line-height: 1.9; margin-top: 12px; }
</style>
</head>
<body>

<section class="panel bottle-label">
  <div class="at" style="top:100px;"><div class="brand-mark"></div></div>
  <div class="at" style="top:196px;"><div class="brand-name">VELORIQUE</div></div>
  <div class="at" style="top:238px;"><div class="brand-line">Inspired by Persian beauty secrets</div></div>
  <div class="at" style="top:314px;"><h1 class="product-name">Light<br>Moisturising<br>Day Cream</h1></div>
  <div class="at" style="top:412px;"><p class="tagline">Climate Adapt<br>Hydration</p></div>
  <div class="at" style="top:464px;"><div class="divider" style="height:38px;"></div></div>
  <div class="at" style="top:520px;"><p class="skin-types">All Skin Types<br>Especially Normal to Combination</p></div>
  <div class="at" style="top:594px;"><div class="motif" role="img" aria-label="Small rose emblem" style="width:32px;height:32px;"></div></div>
  <div class="at" style="top:658px;"><p class="volume">50 ml ℮ 1.69 fl.oz.</p></div>
  <div class="landscape" role="img" aria-label="Layered blush hills with fine rose-gold contour lines"></div>
</section>

<section class="panel carton-front">
  <div class="at" style="top:160px;"><div class="brand-mark"></div></div>
  <div class="at" style="top:278px;"><div class="brand-name">VELORIQUE</div></div>
  <div class="at" style="top:336px;"><div class="brand-line">Inspired by Persian beauty secrets</div></div>
  <div class="at" style="top:384px;"><div class="divider" style="height:70px;"></div></div>
  <div class="at" style="top:494px;"><h2 class="product-name">Light<br>Moisturising<br>Day Cream</h2></div>
  <div class="at" style="top:600px;"><p class="tagline">Climate Adapt<br>Hydration</p></div>
  <div class="at" style="top:676px;"><div class="motif" role="img" aria-label="Small rose emblem" style="width:40px;height:40px;"></div></div>
  <div class="at" style="top:740px;"><p class="skin-types">All Skin Types<br>Especially Normal to Combination</p></div>
  <div class="at" style="top:812px;"><p class="volume">50 ml ℮ 1.69 fl.oz.</p></div>
  <div class="landscape" role="img" aria-label="Layered blush hills with fine rose-gold contour lines"></div>
</section>

<aside class="panel carton-side">
  <div class="benefit" style="top:170px;">
    <svg viewBox="0 0 26 30"><path d="M13 2 C13 2 4 14 4 20 a9 9 0 0 0 18 0 C22 14 13 2 13 2 Z"/></svg>
    <p>Climate Adapt<br>Hydration</p>
  </div>
  <div class="benefit" style="top:305px;">
    <svg viewBox="0 0 26 30"><path d="M5 27 C5 12 12 4 22 3 C22 15 16 24 5 27 Z M5 27 L16 12"/></svg>
    <p>Lightweight<br>Comfort</p>
  </div>
  <div class="benefit" style="top:440px;">
    <svg viewBox="0 0 26 30"><path d="M13 2 L23 6 V14 C23 21 18 26 13 28 C8 26 3 21 3 14 V6 Z M13 2 V28"/></svg>
    <p>Skin Barrier<br>Support</p>
  </div>
  <div class="benefit" style="top:575px;">
    <svg viewBox="0 0 26 30"><path d="M13 3 C14 11 16 13 23 15 C16 17 14 19 13 27 C12 19 10 17 3 15 C10 13 12 11 13 3 Z"/></svg>
    <p>All Day<br>Radiance</p>
  </div>
  <div class="benefit" style="top:705px;">
    <svg viewBox="0 0 26 30"><path d="M13 26 C6 20 3 16 3 11 a5 5 0 0 1 10 -2 a5 5 0 0 1 10 2 C23 16 20 20 13 26 Z"/></svg>
    <p>For All Climates<br>&amp; Skin Types</p>
  </div>
  <div class="landscape" role="img" aria-label="Continuation of layered blush hills"></div>
</aside>

</body>
</html>
```